Business Card & Stationery
Larkspur Renewal
Project: Business Card & Stationery
Business Card & Stationery  - Health
Creative Brief
Simple
Thomas Valdoroni, DNP, RN, APN-C
418 West Birch Avenue Suite 5K Moorestown, NJ 08057
LarkspurRenewal@postvale.example
www.LarkspurRenewal.example
There are two logs attached, one with white background and one with beige background. You can use either color in your design

```html
<!DOCTYPE html>
<html lang="en">
<head>
<meta charset="utf-8">
<title>Larkspur Renewal — Business Cards</title>
<link rel="stylesheet" href="https://fonts.googleapis.com/css2?family=Cormorant+SC:wght@500;600&display=swap">
<style>
  :root {
    --ink: #121212;
    --paper: #ffffff;
    --cream: #fbe8b2;
    --lamp: #f3d41c;
    --edge: #c9c9c9;
    --serif: "Cormorant SC", "Times New Roman", serif;
  }
  * { box-sizing: border-box; margin: 0; padding: 0; }
  html, body { width: 1200px; height: 1049px; overflow: hidden; background: var(--paper); }
  body { position: relative; font-family: var(--serif); color: var(--ink); }

  .card { position: absolute; overflow: hidden; border: 1px solid var(--edge); }
  .card svg.card-bg { position: absolute; inset: 0; width: 100%; height: 100%; }

  .card--front-light { left: 315px; top: 28px; width: 555px; height: 312px; background: var(--paper); }
  .card--front-dark  { left: 39px;  top: 357px; width: 547px; height: 313px; background: var(--paper); }
  .card--back-white  { left: 608px; top: 357px; width: 544px; height: 313px; background: var(--paper); }
  .card--back-black  { left: 39px;  top: 686px; width: 547px; height: 307px; background: var(--ink); border-color: var(--ink); }
  .card--back-cream  { left: 608px; top: 686px; width: 544px; height: 307px; background: var(--cream); }

  .brand { position: absolute; display: flex; align-items: center; gap: 12px; white-space: nowrap; }
  .brand__mark { width: 30px; height: 30px; background: var(--lamp); flex: none; }
  .brand__text { display: flex; flex-direction: column; }
  .brand__name { font-size: 40px; font-weight: 600; line-height: 1; letter-spacing: 1px; }
  .brand__tagline { font-size: 10px; font-weight: 600; letter-spacing: 3px; margin-top: 6px; text-align: center; }
  .brand--small { left: 24px; top: 26px; }
  .brand--small .brand__name { font-size: 30px; }
  .brand--small .brand__mark { width: 26px; height: 26px; }
  .brand--center { left: 50%; top: 50%; transform: translate(-50%, -50%); }
  .brand--on-dark { color: var(--paper); }

  .holder { position: absolute; left: 26px; font-size: 22px; font-weight: 500; letter-spacing: 0.5px; white-space: nowrap; }
  .contact { position: absolute; left: 26px; font-size: 13px; font-weight: 600; line-height: 17px; list-style: none; white-space: nowrap; }
  .contact--on-dark { color: var(--paper); }

  .card--front-light .holder { top: 168px; }
  .card--front-light .contact { top: 214px; }
  .card--front-dark .holder { top: 118px; }
  .card--front-dark .contact { top: 200px; }
</style>
</head>
<body>

  <section class="card card--front-light">
    <svg class="card-bg" viewBox="0 0 555 312" preserveAspectRatio="none" aria-hidden="true">
      <path d="M0 148 C 160 168, 380 150, 555 112 L555 312 L0 312 Z" fill="var(--cream)"/>
      <path d="M0 140 C 160 160, 380 140, 555 96 L555 124 C 380 162, 160 172, 0 150 Z" fill="var(--ink)"/>
    </svg>
    <div class="brand brand--small">
      <span class="brand__mark"></span>
      <div class="brand__text">
        <span class="brand__name">Larkspur Renewal</span>
        <span class="brand__tagline">Caring For Caregivers</span>
      </div>
    </div>
    <p class="holder">Thomas Valdoroni, DNP, RN, APN-C</p>
    <ul class="contact">
      <li>418 West Birch Avenue, Suite 5K</li>
      <li>Ashbrook, NJ 08099</li>
      <li>Phone: 609-555-0148</li>
      <li>Email: LarkspurRenewal@postvale.example</li>
      <li>www.LarkspurRenewal.example</li>
    </ul>
  </section>

  <section class="card card--front-dark">
    <svg class="card-bg" viewBox="0 0 547 313" preserveAspectRatio="none" aria-hidden="true">
      <path d="M0 166 C 170 178, 380 168, 547 132 L547 313 L0 313 Z" fill="var(--cream)"/>
      <path d="M0 172 C 170 184, 380 174, 547 140 L547 313 L0 313 Z" fill="var(--ink)"/>
    </svg>
    <div class="brand brand--small">
      <span class="brand__mark"></span>
      <div class="brand__text">
        <span class="brand__name">Larkspur Renewal</span>
        <span class="brand__tagline">Caring For Caregivers</span>
      </div>
    </div>
    <p class="holder">Thomas Valdoroni, DNP, RN, APN-C</p>
    <ul class="contact contact--on-dark">
      <li>418 West Birch Avenue, Suite 5K</li>
      <li>Ashbrook, NJ 08099</li>
      <li>Phone: 609-555-0148</li>
      <li>Email: LarkspurRenewal@postvale.example</li>
      <li>www.LarkspurRenewal.example</li>
    </ul>
  </section>

  <section class="card card--back-white">
    <div class="brand brand--center">
      <span class="brand__mark"></span>
      <div class="brand__text">
        <span class="brand__name">Larkspur Renewal</span>
        <span class="brand__tagline">Caring For Caregivers</span>
      </div>
    </div>
  </section>

  <section class="card card--back-black">
    <div class="brand brand--center brand--on-dark">
      <span class="brand__mark"></span>
      <div class="brand__text">
        <span class="brand__name">Larkspur Renewal</span>
        <span class="brand__tagline">Caring For Caregivers</span>
      </div>
    </div>
  </section>

  <section class="card card--back-cream">
    <div class="brand brand--center">
      <span class="brand__mark"></span>
      <div class="brand__text">
        <span class="brand__name">Larkspur Renewal</span>
        <span class="brand__tagline">Caring For Caregivers</span>
      </div>
    </div>
  </section>

</body>
</html>
```